Business Card for Yachting Management Company

Need a business card design for a new yachting project management company. Attached is the logo for the company.
Our clients are large yacht owners and captains.
Design must be in the style of the logo. Modern, elegant.

Example of data to show:
Oliver Tennant
Project Manager
(+34) 612 870 334
oliver@quarvel.net
Quarvel Management - Marisol Tower, Office 22 - NDR - Palma de Mallorca

The data above will have to be changed (by me) for the different people in the company over the next years.

Will be printed using CardHarbor (Lustrel Business Cards). They provide these guidelines for the size:
"the actual size of the card is 1050 x 600 pixels. However, the full bleed size is 1083 x 633 pixels, and the safe printing area is 1008 x 558 pixels."

```html
<!DOCTYPE html>
<html lang="en">
<head>
<meta charset="utf-8">
<title>Quarvel Management – Business Card</title>
<link href="https://fonts.googleapis.com/css2?family=Nunito:wght@400;600;700&display=swap" rel="stylesheet">
<style>
  :root {
    --brand-blue: #0b74bb;
    --brand-grey: #808080;
    --card-white: #ffffff;
    --canvas-bg: #e9e9e9;
  }
  html, body {
    margin: 0;
    width: 1200px;
    height: 1200px;
    overflow: hidden;
    background: var(--canvas-bg);
  }
  .business-card {
    position: absolute;
    left: 75px;
    top: 300px;
    width: 1050px;
    height: 600px;
    display: block;
    font-family: "Nunito", sans-serif;
  }
  .card-base { fill: var(--card-white); }
  .info-band { fill: var(--brand-blue); }
  .accent-sail { fill: var(--brand-grey); }
  .brand-name { fill: var(--brand-blue); font-weight: 700; }
  .person-name { fill: var(--brand-grey); font-weight: 700; font-size: 30px; letter-spacing: 2px; }
  .person-role { fill: var(--card-white); font-weight: 600; font-size: 24px; }
  .contact-phone { fill: var(--card-white); font-weight: 600; font-size: 23px; }
  .contact-email { fill: var(--card-white); font-weight: 600; font-size: 20px; }
  .contact-address { fill: var(--card-white); font-weight: 600; font-size: 18px; }
</style>
</head>
<body>
<svg class="business-card" viewBox="0 0 1050 600" xmlns="http://www.w3.org/2000/svg" aria-label="Quarvel Management business card">
  <rect class="card-base" x="0" y="0" width="1050" height="600"/>
  <!-- blue band with speech-bubble notch -->
  <path class="info-band" d="M0 300 H696 V413 L778 300 H1050 V600 H0 Z"/>
  <!-- grey sail accent -->
  <path class="accent-sail" d="M88 300 L171 186 V300 Z"/>

  <g class="brand-lockup">
    <rect class="brand-name" x="696" y="104" width="22" height="22"/>
    <text class="brand-name" x="969" y="150" text-anchor="end" font-size="66">Quarvel</text>
    <text class="brand-name" x="969" y="222" text-anchor="end" font-size="34" letter-spacing="4">Management</text>
  </g>

  <text class="person-name" x="181" y="294">OLIVER TENNANT</text>
  <text class="person-role" x="181" y="326">Project Manager</text>

  <text class="contact-phone" x="181" y="490">(+34) 612 870 334</text>
  <text class="contact-email" x="181" y="518">oliver@quarvel.net</text>
  <text class="contact-address" x="180" y="554">Quarvel Management - Marisol Tower, Office 22 - NDR - Palma de Mallorca</text>
</svg>
</body>
</html>
```